2 page flyer for a turf supply company. TAMBREL TURF SOLUTIONS

Design a marketing flyer to be distributed to landscaping contractors, councils, and private users.
I have attached a Dropbox link that holds the logo files, copy, and brand guidelines and images.
I am wanting the brochure to be 2 pages, which can be sent as a pdf or printed double-sided. I would like a modern, professional look using the colours from the brand guidelines. We are designing a new website so this brochure will be found on the website as well as sent to clients. I have uploaded the copy, a logo, and brand guidelines. The link to more photos and logos are found on the Dropbox link below.
https://www.filecrate-share.net/fo/k29dmx7qpw4vzt/h?key=xq81trbnvw0l6cj&dl=0
Here is the link to the current website. https://tambrelgroup.com.au/
New one coming.

Target Market(s)

The decision makers at councils, landscape businesses and land developers

Industry/Entity Type

landscaping companies and councils

Font styles to use
Sans Serif

Requirements
Must have
• must be eye catching and easy to read
Nice to have
• Bold headings

```html
<!DOCTYPE html>
<html lang="en">
<head>
<meta charset="utf-8">
<title>Tambrel Turf Solutions – Flyer</title>
<link href="https://fonts.googleapis.com/css2?family=Poppins:ital,wght@0,300;0,400;0,500;0,600;0,700;0,800;1,300&display=swap" rel="stylesheet">
<style>
  :root{
    --stage:#858384;
    --navy:#1b5677;
    --navy-deep:#134463;
    --navy-ink:#163c55;
    --green:#8cc63f;
    --green-dark:#2f6e34;
    --cream:#f3f6e9;
    --paper:#fbfcf7;
    --white:#ffffff;
    --body-light:#d9e4ec;
    --ink:#222a30;
  }
  *{box-sizing:border-box;margin:0;padding:0}
  html,body{width:1200px;height:799px;overflow:hidden}
  body{background:var(--stage);font-family:"Poppins",sans-serif;position:relative}
  .side-label{position:absolute;top:42px;color:var(--white);font-weight:700;font-size:25px;letter-spacing:.5px;transform:translateX(-50%)}
  .page{position:absolute;top:87px;overflow:hidden;background:var(--white)}
  .page--front{left:95px;width:508px;height:657px}
  .page--back{left:636px;width:510px;height:659px}
  .abs{position:absolute}

  /* shared */
  .grass{position:absolute;background:linear-gradient(180deg,rgba(140,198,63,0) 0%,#8cc63f 45%,#4f9a2c 100%)}
  .icon-ring{position:absolute;width:34px;height:34px;border:1.3px solid var(--green);border-radius:50%;display:flex;align-items:center;justify-content:center}
  .feature-title{position:absolute;color:var(--white);font-weight:700;font-size:11px;line-height:13.8px;letter-spacing:.1px}
  .feature-body{position:absolute;color:var(--body-light);font-weight:300;font-size:7.7px;line-height:8.85px}
  .green-tab{position:absolute;left:26px;width:62px;height:6px;border-radius:3px;background:var(--green)}

  /* footer */
  .footer{position:absolute;left:0;right:0;bottom:0;height:71px;background:var(--cream)}
  .footer__shape{position:absolute;left:0;top:0}
  .brand{position:absolute;left:24px;top:15px;display:flex;align-items:center;gap:6px;color:var(--navy)}
  .brand__dot{width:38px;height:38px;border-radius:50%;background:var(--navy)}
  .brand__name{font-weight:700;line-height:1}
  .brand__name span{display:block}
  .brand__name .big{font-size:19px}
  .brand__name .small{font-size:10.3px;letter-spacing:.6px;margin-top:2px}
  .contact-label{position:absolute;left:225px;top:26px;color:var(--white);font-weight:500;font-size:14px;letter-spacing:.3px}
  .contact-rule{position:absolute;left:321px;top:14px;width:1px;height:48px;background:rgba(255,255,255,.8)}
  .contact-list{position:absolute;left:336px;top:15px;list-style:none;color:var(--white);font-weight:600;font-size:10px;line-height:12.4px}
  .contact-list li{display:flex;align-items:center;gap:6px}
  .contact-list svg{width:8px;height:8px;flex:none}

  /* front */
  .hero-photo{left:0;top:0;width:508px;height:222px;clip-path:polygon(142px 0,508px 0,508px 222px,0 222px,0 53px,166px 53px);
    background:linear-gradient(180deg,#3d8fd0 0%,#9fc8e6 12%,#6a9a5a 20%,#8fb84a 45%,#a9c93c 62%,#5f8c2b 100%)}
  .hero-grass{left:0;top:30px;width:168px;height:24px}
  .headline{position:absolute;left:25px;top:64px;color:var(--white);font-weight:800;font-size:20.3px;line-height:21.4px;letter-spacing:-.1px}
  .welcome{position:absolute;left:0;top:163px;width:508px;height:59px;background:var(--cream)}
  .welcome__text{position:absolute;left:27px;top:10px;font-size:9.3px;line-height:11px;color:#3b4650}
  .welcome__text em{font-style:normal;color:var(--green);font-weight:600}
  .welcome__band{position:absolute;left:0;top:0}
  .welcome__claim{position:absolute;left:260px;top:10px;width:240px;color:var(--white);font-size:8.5px;line-height:9.9px}
  .main{position:absolute;left:0;top:221px;width:508px;height:365px;background:linear-gradient(160deg,#1e5d7c 0%,var(--navy) 45%,var(--navy-deep) 100%)}
  .cta-pill{position:absolute;left:273px;top:532px;width:223px;height:14px;border-radius:7px;background:var(--navy-ink);color:var(--white);font-size:6.9px;font-weight:700;display:flex;align-items:center;justify-content:center}
  .cta-pill b{color:var(--green);margin-right:2px}

  /* back */
  .varieties-bg{left:0;top:40px;width:510px;height:283px;background:linear-gradient(180deg,var(--navy) 0%,var(--navy-deep) 100%)}
  .top-grass{left:220px;top:18px;width:290px;height:24px}
  .varieties-title{position:absolute;left:25px;top:36px;color:var(--white);font-weight:800;font-size:20px;line-height:28px}
  .photo-frame{position:absolute;left:23px;width:187px;border:3px solid var(--white);border-radius:10px}
  .photo-skate{top:154px;height:90px;background:linear-gradient(180deg,#2f7fd3 0%,#8cb9e4 40%,#c8a79c 62%,#b8918a 78%,#6ea345 100%)}
  .photo-field{top:250px;height:89px;background:linear-gradient(180deg,#6a97b9 0%,#7f9a7c 22%,#5ea43c 40%,#4c9a2f 100%)}
  .variety-line{left:243px;top:80px;width:1px;height:213px;background:rgba(255,255,255,.35)}
  .check{position:absolute;left:236px;width:13px;height:13px}
  .variety-title{position:absolute;left:255px;color:var(--white);font-weight:700;font-size:11.3px;line-height:13.5px}
  .variety-body{position:absolute;left:255px;width:234px;color:var(--body-light);font-weight:300;font-size:7.6px;line-height:8.9px}
  .lower{left:0;top:323px;width:510px;height:336px;background:var(--paper)}
  .park-photo{left:248px;top:325px;width:262px;height:72px;border-bottom-left-radius:60px 72px;
    background:linear-gradient(180deg,#4d8fd6 0%,#b3cce6 35%,#5f8f3a 60%,#7fb04a 100%)}
  .testimonials-title{position:absolute;left:27px;top:358px;color:var(--navy);font-weight:700;font-size:14px}
  .quote-card{position:absolute;left:29px;width:227px;height:46px;border:1px solid var(--navy);border-radius:8px;background:var(--white)}
  .quote-card__mark{position:absolute;left:16px;top:-9px;padding:0 2px;background:var(--paper);color:var(--green);font-weight:800;font-size:17px;line-height:14px}
  .quote-card__text{position:absolute;left:15px;top:8px;width:200px;font-style:italic;font-weight:300;font-size:7.5px;line-height:8.9px;color:#33404a}
  .quote-card__name{position:absolute;left:114px;top:39px;width:98px;height:12px;border-radius:6px;background:var(--navy);color:var(--white);font-size:7.3px;font-weight:600;display:flex;align-items:center;justify-content:center}
  .services-title{position:absolute;left:282px;top:420px;color:var(--navy);font-weight:700;font-size:14.8px;line-height:18.5px}
  .services-title em{font-style:normal;color:var(--green)}
  .services-list{position:absolute;left:286px;top:463px;list-style:none;color:var(--ink);font-weight:500;font-size:9.4px;line-height:14.3px}
  .services-list li{position:relative;padding-left:10px}
  .services-list li svg{position:absolute;left:0;top:3.5px;width:8px;height:8px}
</style>
</head>
<body>

<div class="side-label" style="left:335px">FRONT</div>
<div class="side-label" style="left:890px">BACK</div>

<!-- FRONT PAGE -->
<section class="page page--front">
  <div class="abs hero-photo" role="img" aria-label="Aerial photo of green turf farm fields beside a river under blue sky"></div>
  <div class="grass hero-grass" role="img" aria-label="Close-up blades of grass"></div>

  <svg class="abs" style="left:0;top:53px" width="300" height="111" viewBox="0 0 300 111" aria-hidden="true">
    <defs>
      <linearGradient id="heroPanel" x1="0" x2="1" y1="0" y2="0">
        <stop offset="0" stop-color="#7cc242"/>
        <stop offset=".55" stop-color="#3b8a63"/>
        <stop offset="1" stop-color="#1d5a7a"/>
      </linearGradient>
    </defs>
    <path d="M0 0 H238 C258 0 262 20 270 45 L292 110 H0 Z" fill="url(#heroPanel)"/>
  </svg>
  <h1 class="headline">DISCOVER THE<br>GREEN DIFFERENCE<br>WITH TAMBREL<br>TURF SOLUTIONS</h1>

  <div class="welcome">
    <svg class="welcome__band" width="508" height="59" viewBox="0 0 508 59" aria-hidden="true">
      <defs>
        <linearGradient id="claimBand" x1="0" x2="1">
          <stop offset="0" stop-color="#1e4d36"/>
          <stop offset="1" stop-color="#2f7a34"/>
        </linearGradient>
      </defs>
      <path d="M217 0 H508 V55 H280 C250 55 240 40 232 25 Z" fill="url(#claimBand)"/>
    </svg>
    <p class="welcome__text">Welcome to Tambrel Turf Solutions (TTS)<br>– your gateway to a vibrant,<br><em>green landscape!</em></p>
    <p class="welcome__claim">With over two decades of expertise in the turf industry, we are your trusted partner for superior turf solutions.</p>
  </div>
  <div class="green-tab" style="top:219px"></div>

  <div class="main"></div>

  <!-- left column -->
  <div class="icon-ring" style="left:27px;top:239px">
    <svg width="18" height="18" viewBox="0 0 18 18" fill="none" stroke="#fff" stroke-width="1"><path d="M2 15 C4 10 5 8 4 4 M6 15 C7 9 8 6 9 3 M10 15 C10 10 12 7 15 5 M13 15 C14 12 15 10 17 9 M1 15 H17"/></svg>
  </div>
  <h2 class="feature-title" style="left:68px;top:244px">PREMIUM TURF PRODUCTS<br>ACROSS NSW</h2>
  <p class="feature-body" style="left:27px;top:279px;width:218px">Over the years, our commitment to excellence has propelled us to supply premium turf products across New South Wales. Our diverse clientele includes professional sporting fields, Council parks, housing estate playing fields, public parks and gardens, as well as domestic gardens and landscaping projects</p>

  <div class="icon-ring" style="left:27px;top:345px">
    <svg width="18" height="18" viewBox="0 0 18 18" fill="none" stroke="#fff" stroke-width="1"><path d="M9 2 L10 4.5 L12.5 4.7 L10.6 6.3 L11.2 8.8 L9 7.5 L6.8 8.8 L7.4 6.3 L5.5 4.7 L8 4.5 Z"/><path d="M2 15 L6 12 H11 L15 10 M6 12 V10 M9 12 V10 M12 11 V9"/></svg>
  </div>
  <h2 class="feature-title" style="left:68px;top:355px">THE TAMBREL ADVANTAGE</h2>
  <p class="feature-body" style="left:27px;top:385px;width:218px">What sets our turf apart is its origin – meticulously grown in the rich alluvial soils of the fertile Richmond Lowlands, ensuring the cultivation of top-tier turf characterised by quality, resilience, and durability. Spanning approximately 300 acres along the Hawkesbury River, Tambrel Turf Solutions boasts one of the largest turf farm land owners in the district. Our expansive land, coupled with full irrigation capabilities, positions TTS as a reliable source of drought-resistant turf supplies</p>

  <div class="icon-ring" style="left:27px;top:478px">
    <svg width="18" height="18" viewBox="0 0 18 18" fill="none" stroke="#fff" stroke-width="1"><path d="M9 1.5 L11 6 L16 6.4 L12.2 9.6 L13.4 14.5 L9 11.8 L4.6 14.5 L5.8 9.6 L2 6.4 L7 6 Z"/><circle cx="9" cy="8.6" r="2"/></svg>
  </div>
  <h2 class="feature-title" style="left:68px;top:489px">DEDICATION TO EXCELLENCE</h2>
  <p class="feature-body" style="left:27px;top:518px;width:212px">At Tambrel Turf Solutions, we are dedicated to providing the highest standard of turf for a wide range of applications. Our commitment goes beyond delivering turf – it's about transforming spaces into green havens that stand the test of time.</p>

  <!-- right column -->
  <div class="icon-ring" style="left:273px;top:239px">
    <svg width="18" height="18" viewBox="0 0 18 18" fill="none" stroke="#fff" stroke-width="1"><circle cx="10" cy="5" r="3"/><path d="M9 8 V10 H11 V8 M2 14 L5 12 H10 L14 10 M10 1 V0"/></svg>
  </div>
  <h2 class="feature-title" style="left:314px;top:244px">TAILORED SOLUTIONS<br>FOR EVERY SPACE</h2>
  <p class="feature-body" style="left:273px;top:279px;width:214px">Tambrel Turf Solutions offers a range of turf varieties. Our commitment to quality extends to providing thick-cut turf, available in convenient maxi rolls or standard turf rolls. No matter the size of your project, we've got the perfect solution to bring your vision to life.</p>

  <div class="icon-ring" style="left:273px;top:346px">
    <svg width="18" height="18" viewBox="0 0 18 18" fill="none" stroke="#fff" stroke-width="1"><path d="M9 16 V6 M9 9 C6 9 4 7 4 4 C7 4 9 6 9 9 M9 7 C11 7 13 5 13 2 C10 2 9 4 9 7 M4 16 H14"/></svg>
  </div>
  <h2 class="feature-title" style="left:314px;top:350px">VERSATILITY WITH<br>CONTRACT GROWING</h2>
  <p class="feature-body" style="left:273px;top:385px;width:214px">Need a specialised turf solution tailored to your unique specifications? Our contract growing services ensure that you get precisely what you order. We work closely with our clients, offering customized growing solutions to meet specific requirements, ensuring a seamless integration with your landscaping plans.</p>

  <div class="icon-ring" style="left:273px;top:452px">
    <svg width="18" height="18" viewBox="0 0 18 18" fill="none" stroke="#fff" stroke-width="1"><circle cx="9" cy="10" r="4.5"/><path d="M7 10 L8.5 11.5 L11.2 8.6 M3 3 L4 4 M15 3 L14 4 M9 1 V3"/></svg>
  </div>
  <h2 class="feature-title" style="left:314px;top:456px">UNMATCHED QUALITY<br>AND EXPERTISE</h2>
  <p class="feature-body" style="left:273px;top:490px;width:226px">At Tambrel Turf Solutions, we don't just provide turf – we deliver a promise of quality, resilience, and expertise. Our team is dedicated to ensuring your satisfaction, from the initial consultation to the delivery of the perfect turf for your space</p>
  <div class="cta-pill"><b>Contact us today</b> and experience the Tambrel Advantage!</div>

  <div class="grass" style="left:261px;top:563px;width:247px;height:24px" role="img" aria-label="Close-up blades of grass"></div>
  <div class="green-tab" style="top:581px"></div>

  <footer class="footer">
    <svg class="footer__shape" width="508" height="71" viewBox="0 0 508 71" aria-hidden="true">
      <path d="M165 71 C185 20 200 0 245 0 H508 V71 Z" fill="#8cc63f"/>
    </svg>
    <div class="brand">
      <span class="brand__dot"></span>
      <span class="brand__name"><span class="big">TAMBREL</span><span class="small">TURF SOLUTIONS</span></span>
    </div>
    <div class="contact-label">CONACT US</div>
    <div class="contact-rule"></div>
    <ul class="contact-list">
      <li><svg viewBox="0 0 10 10" fill="none" stroke="#fff" stroke-width="1"><path d="M2 1 L4 1 L5 3.5 L3.8 4.5 C4.4 5.7 5.3 6.6 6.5 7.2 L7.5 6 L9.5 7 V9 C5 9 1 5 1 1.5 Z"/></svg>0400 317 642</li>
      <li><svg viewBox="0 0 10 10" fill="none" stroke="#fff" stroke-width="1"><rect x="1" y="2" width="8" height="6"/><path d="M1 2 L5 5.5 L9 2"/></svg>turf@tambrelgroup.com.au</li>
      <li><svg viewBox="0 0 10 10" fill="none" stroke="#fff" stroke-width="1"><circle cx="5" cy="5" r="4"/><path d="M1 5 H9 M5 1 C3 3.5 3 6.5 5 9 M5 1 C7 3.5 7 6.5 5 9"/></svg>tambrelgroup.com.au</li>
    </ul>
  </footer>
</section>

<!-- BACK PAGE -->
<section class="page page--back">
  <div class="grass abs top-grass" role="img" aria-label="Close-up blades of grass"></div>
  <div class="abs varieties-bg"></div>
  <svg class="abs" style="left:0;top:24px" width="230" height="112" viewBox="0 0 230 112" aria-hidden="true">
    <defs>
      <linearGradient id="titlePanel" x1="0" x2="1">
        <stop offset="0" stop-color="#1d5a7a"/>
        <stop offset=".55" stop-color="#4d9a4a"/>
        <stop offset="1" stop-color="#8cc63f"/>
      </linearGradient>
    </defs>
    <path d="M0 0 H225 L200 70 C190 100 180 111 160 111 H0 Z" fill="url(#titlePanel)"/>
  </svg>
  <h2 class="varieties-title">Turf Varieties<br>grown and<br>available</h2>

  <div class="photo-frame photo-skate" role="img" aria-label="Photo of a concrete skate park bordered by fresh turf"></div>
  <div class="photo-frame photo-field" role="img" aria-label="Photo of a newly turfed green sports field"></div>

  <div class="abs variety-line"></div>
  <svg class="check" style="top:65px" viewBox="0 0 13 13"><circle cx="6.5" cy="6.5" r="6.5" fill="#8cc63f"/><path d="M3.5 6.7 L5.6 8.7 L9.5 4.6" stroke="#fff" stroke-width="1.5" fill="none"/></svg>
  <h3 class="variety-title" style="top:64px">SANTA ANNA COUCH</h3>
  <p class="variety-body" style="top:80px">Known for its resilience and fine texture, Santa Anna Couch is a versatile turf variety ideal for creating lush, green landscapes that can withstand various environmental conditions.</p>

  <svg class="check" style="top:119px" viewBox="0 0 13 13"><circle cx="6.5" cy="6.5" r="6.5" fill="#8cc63f"/><path d="M3.5 6.7 L5.6 8.7 L9.5 4.6" stroke="#fff" stroke-width="1.5" fill="none"/></svg>
  <h3 class="variety-title" style="top:118px">WINTERGREEN COUCH</h3>
  <p class="variety-body" style="top:135px">Wintergreen Couch is prized for its vibrant green colour and dense growth, making it a popular choice for lawns and sports fields, providing a soft and inviting surface.</p>

  <svg class="check" style="top:173px" viewBox="0 0 13 13"><circle cx="6.5" cy="6.5" r="6.5" fill="#8cc63f"/><path d="M3.5 6.7 L5.6 8.7 L9.5 4.6" stroke="#fff" stroke-width="1.5" fill="none"/></svg>
  <h3 class="variety-title" style="top:172px">KIKUYU</h3>
  <p class="variety-body" style="top:188px">Renowned for its rapid growth, durability, and ability to thrive in various climates, Kikuyu turf is a popular choice for lawns, sports fields, and recreational areas, providing a resilient and vibrant green surface.</p>

  <svg class="check" style="top:237px" viewBox="0 0 13 13"><circle cx="6.5" cy="6.5" r="6.5" fill="#8cc63f"/><path d="M3.5 6.7 L5.6 8.7 L9.5 4.6" stroke="#fff" stroke-width="1.5" fill="none"/></svg>
  <h3 class="variety-title" style="top:236px">OVERSOWN RYE GRASS BLENDS<br>(OVERSOWN TO ORDER):</h3>
  <p class="variety-body" style="top:267px">Our Oversown Rye Grass Blends are tailored to order, offering a flexible solution for enhancing turf durability and maintaining a lush appearance, especially during colder seasons.</p>

  <div class="abs lower"></div>
  <div class="abs park-photo" role="img" aria-label="Photo of a park with trees, lawn and a winding footpath"></div>

  <h2 class="testimonials-title">Testimonials</h2>
  <div class="quote-card" style="top:386px">
    <span class="quote-card__mark">“</span>
    <p class="quote-card__text">Lorem Ipsum is simply dummy text of the printing and typesetting industry. Lorem Ipsum has been the industry's standard dummy text ever since the 1500s,</p>
    <span class="quote-card__name">- Lorem duumy</span>
  </div>
  <div class="quote-card" style="top:445px">
    <span class="quote-card__mark">“</span>
    <p class="quote-card__text">Lorem Ipsum is simply dummy text of the printing and typesetting industry. Lorem Ipsum has been the industry's standard dummy text ever since the 1500s,</p>
    <span class="quote-card__name">- Lorem duumy</span>
  </div>
  <div class="quote-card" style="top:503px">
    <span class="quote-card__mark">“</span>
    <p class="quote-card__text">Lorem Ipsum is simply dummy text of the printing and typesetting industry. Lorem Ipsum has been the industry's standard dummy text ever since the 1500s,</p>
    <span class="quote-card__name">- Lorem duumy</span>
  </div>

  <h2 class="services-title">Tambrel <em>Turf Solutions</em><br>Services:</h2>
  <ul class="services-list">
    <li><svg viewBox="0 0 8 8"><circle cx="4" cy="4" r="4" fill="#8cc63f"/><path d="M2.2 4.1 L3.5 5.3 L5.9 2.8" stroke="#fff" stroke-width="1" fill="none"/></svg>Turf supply</li>
    <li><svg viewBox="0 0 8 8"><circle cx="4" cy="4" r="4" fill="#8cc63f"/><path d="M2.2 4.1 L3.5 5.3 L5.9 2.8" stroke="#fff" stroke-width="1" fill="none"/></svg>Domestic &amp; commercial sales</li>
    <li><svg viewBox="0 0 8 8"><circle cx="4" cy="4" r="4" fill="#8cc63f"/><path d="M2.2 4.1 L3.5 5.3 L5.9 2.8" stroke="#fff" stroke-width="1" fill="none"/></svg>Thick cut turf, supplied in either<br>maxi rolls or standard turf rolls</li>
    <li><svg viewBox="0 0 8 8"><circle cx="4" cy="4" r="4" fill="#8cc63f"/><path d="M2.2 4.1 L3.5 5.3 L5.9 2.8" stroke="#fff" stroke-width="1" fill="none"/></svg>Contract growing</li>
    <li><svg viewBox="0 0 8 8"><circle cx="4" cy="4" r="4" fill="#8cc63f"/><path d="M2.2 4.1 L3.5 5.3 L5.9 2.8" stroke="#fff" stroke-width="1" fill="none"/></svg>Pick up or delivery</li>
  </ul>

  <div class="grass" style="left:260px;top:566px;width:250px;height:25px" role="img" aria-label="Close-up blades of grass"></div>

  <footer class="footer" style="height:68px;background:var(--paper)">
    <svg class="footer__shape" width="510" height="68" viewBox="0 0 510 68" aria-hidden="true">
      <path d="M166 68 C186 18 200 0 246 0 H510 V68 Z" fill="#8cc63f"/>
    </svg>
    <div class="brand">
      <span class="brand__dot"></span>
      <span class="brand__name"><span class="big">TAMBREL</span><span class="small">TURF SOLUTIONS</span></span>
    </div>
    <div class="contact-label">CONACT US</div>
    <div class="contact-rule"></div>
    <ul class="contact-list">
      <li><svg viewBox="0 0 10 10" fill="none" stroke="#fff" stroke-width="1"><path d="M2 1 L4 1 L5 3.5 L3.8 4.5 C4.4 5.7 5.3 6.6 6.5 7.2 L7.5 6 L9.5 7 V9 C5 9 1 5 1 1.5 Z"/></svg>0400 317 642</li>
      <li><svg viewBox="0 0 10 10" fill="none" stroke="#fff" stroke-width="1"><rect x="1" y="2" width="8" height="6"/><path d="M1 2 L5 5.5 L9 2"/></svg>turf@tambrelgroup.com.au</li>
      <li><svg viewBox="0 0 10 10" fill="none" stroke="#fff" stroke-width="1"><circle cx="5" cy="5" r="4"/><path d="M1 5 H9 M5 1 C3 3.5 3 6.5 5 9 M5 1 C7 3.5 7 6.5 5 9"/></svg>tambrelgroup.com.au</li>
    </ul>
  </footer>
</section>

</body>
</html>
```